Erklär-Flyer für Gutschein-Ankauf-Service Bonkarten-Profi.de
Zielgruppe
Auf http://www.bonkarten-profi.de/ bieten wir u.a. den Service an, ungenutzte Geschenkkarten von großen Händlern wie z.B. Technoplatz, Vandoro, WOLM, usw. direkt gegen Bargeld einzutauschen. Diesen Service wollen wir nun in einem Flyer vorstellen.
Die Zielgruppe des zu erstellenden Flyers sollen vor allem Mitarbeiter bei Firmen z.B. Auto Verkäufer sein, die von Ihrem Arbeitgeber als Prämie Geschenkgutscheine als Incentive erhalten und diese aber lieber in Bargeld umtauschen würden.
Das Wunschszenario wäre: Wir schicken den Flyer zusammen mit einem Anschreiben an die jeweiligen Firmen. Der/diejenige die den Brief und Flyer entgegennimmt, erkennt den Sinn und Nutzen und gibt den Flyer an Ihre Kollegen weiter bzw. hängt ihn ans schwarze Brett etc.
Aufgabenstellung
Gestaltet werden soll ein 3 Schritte Falz-Flyer (z.B. 6-seitiger Altarfalz Fensterfalz) angelehnt an das bisherige Design auf Bonkarten-Profi.de (nicht zwingend 100%, gerne auch eigene Ideen). Auf der Außenseite nur kurz in einem Satz um was es geht und auf der Innenseite dann am Besten in 3 Schritten erklärt, wie einfach der Umtausch von Gutscheinen in Bargeld ist.
Das Wichtigste ist die "Bequemlichkeit, Einfachheit, kein Aufwand", am zweitwichtigsten ist "Sicherheit, Seriosität" (Unsere Seite gibt es schon seit 2008 und wir wurden bereits im KRT vorgestellt).
Verteilung des Falt-Flyer als Brief mit der Post. Wenn der Brief geöffnet wird ist der zu erreichende Optimal Zustand, dass der Flyer von der Person, die den Brief öffnet, z.B. ans "schwarze Brett" gehängt wird als Info bzw. eine Art Anleitung.

```html
<!DOCTYPE html>
<html lang="de">
<head>
<meta charset="utf-8">
<title>Bonkarten-Profi – Altarfalz-Flyer</title>
<link rel="stylesheet" href="https://fonts.googleapis.com/css2?family=Montserrat:wght@500;600&family=Roboto:wght@400;700&display=swap">
<style>
  :root {
    --ink: #2b2b2b;
    --line: #333333;
    --brand-blue: #1a63a8;
    --badge-blue: #0f4fa0;
    --brand-green: #8dc21f;
    --sky-top: #a9d3ef;
    --sky-bottom: #dcecf7;
    --diagram-fill: #eef0f2;
    --white: #ffffff;
  }
  * { margin: 0; padding: 0; box-sizing: border-box; }
  html, body { width: 1200px; height: 699px; overflow: hidden; background: var(--white); }
  body { position: relative; font-family: "Roboto", Arial, sans-serif; color: var(--ink); }

  .fold-title {
    position: absolute; left: 16px; top: 6px;
    font-family: "Montserrat", Arial, sans-serif; font-weight: 600; font-size: 16px;
  }
  .fold-scheme {
    position: absolute; left: 14px; top: 44px; width: 638px; height: 149px;
    background: var(--diagram-fill);
  }
  .format-label {
    position: absolute; top: 231px;
    font-family: "Montserrat", Arial, sans-serif; font-weight: 500; font-size: 13px;
  }
  .format-label.open { left: 18px; }
  .format-label.closed { left: 506px; }
  .format-arrow { position: absolute; left: 14px; top: 246px; }

  /* Front cover */
  .cover {
    position: absolute; left: 45px; top: 306px; width: 248px; height: 348px; overflow: hidden;
    background: linear-gradient(160deg, #e7ecef 0%, #d8b79b 40%, #a88870 62%, #9cc7df 100%);
  }
  .cover-photo { position: absolute; inset: 0; }
  .brand-name {
    position: absolute; left: 10px; top: 16px;
    font-weight: 700; font-size: 15px; line-height: 1.1; color: var(--brand-blue);
  }
  .claim-badge {
    position: absolute; left: -18px; top: 66px; width: 78px; height: 80px; border-radius: 50%;
    background: var(--brand-green); color: var(--white);
    font-size: 11px; line-height: 1.4; padding: 17px 0 0 27px;
  }
  .headline-badge {
    position: absolute; left: 186px; top: 281px; width: 118px; height: 118px; border-radius: 50%;
    transform: translate(-50%, -50%);
    background: var(--badge-blue); color: var(--white); text-align: center;
    padding-top: 26px;
  }
  .headline-badge .kicker { font-size: 11px; line-height: 1.2; }
  .headline-badge .main { font-weight: 700; font-size: 17px; line-height: 1.15; margin-top: 4px; }

  /* Inside spread */
  .inside {
    position: absolute; left: 675px; top: 308px; width: 493px; height: 348px; overflow: hidden;
    background: linear-gradient(180deg, var(--sky-top) 0%, var(--sky-bottom) 70%, #c7e0f1 100%);
  }
  .inside-art { position: absolute; left: 0; top: 0; }
  .step-number { font-weight: 700; font-size: 34px; fill: var(--white); }
  .inside-brand {
    position: absolute; right: 14px; top: 20px;
    font-weight: 700; font-size: 9px; color: var(--brand-blue);
  }
  .step-text {
    position: absolute; top: 262px; font-size: 5.6px; line-height: 1.35; color: #1f3c66;
  }
  .step-text strong { font-weight: 700; }
  .step-text.one { left: 11px; width: 110px; }
  .step-text.two { left: 215px; width: 130px; top: 257px; }
  .step-text.three { left: 377px; width: 105px; }
  .fold-line { position: absolute; top: 294px; width: 1px; height: 380px; background: #9aa5ad; }
</style>
</head>
<body>
  <div class="fold-title">6-seitiger Altarfalz (Fensterfalz)</div>
  <div class="fold-scheme" role="img" aria-label="Falzschema: sechsseitiger Altarfalz vom offenen zum geschlossenen Format"></div>

  <div class="format-label open">offenes Format</div>
  <div class="format-label closed">geschlossenes Format</div>
  <svg class="format-arrow" width="640" height="8" viewBox="0 0 640 8" aria-hidden="true">
    <line x1="0" y1="4" x2="634" y2="4" stroke="var(--line)" stroke-width="1.2"/>
    <polygon points="632,1 638,4 632,7" fill="var(--line)"/>
  </svg>

  <section class="cover">
    <div class="cover-photo" role="img" aria-label="Foto: lächelnde Frau mit Einkaufstüten über der Schulter"></div>
    <div class="brand-name">Bonkarten-Profi</div>
    <div class="claim-badge">einfach.<br>schnell.<br>seriös.</div>
    <div class="headline-badge">
      <div class="kicker">Machen Sie<br>ungenutze</div>
      <div class="main">Gutscheine<br>zu Geld</div>
    </div>
  </section>

  <section class="inside">
    <svg class="inside-art" width="493" height="348" viewBox="0 0 493 348">
      <defs>
        <linearGradient id="photo-check" x1="0" y1="0" x2="1" y2="1">
          <stop offset="0" stop-color="#f4f6f4"/><stop offset="1" stop-color="#cfd9cf"/>
        </linearGradient>
        <linearGradient id="photo-keys" x1="0" y1="0" x2="0" y2="1">
          <stop offset="0" stop-color="#d8dde1"/><stop offset="0.5" stop-color="#5fae45"/><stop offset="1" stop-color="#b9c0c5"/>
        </linearGradient>
        <linearGradient id="photo-woman" x1="0" y1="0" x2="1" y2="1">
          <stop offset="0" stop-color="#f0f2f3"/><stop offset="0.5" stop-color="#8a5a44"/><stop offset="1" stop-color="#e8ecee"/>
        </linearGradient>
      </defs>
      <g stroke="var(--brand-green)" stroke-width="3">
        <polygon points="0,110 104,110 124,177 104,244 0,244" fill="url(#photo-check)" role="img" aria-label="Foto: Checkliste mit grünem Stift"/>
        <polygon points="112,110 348,110 368,177 348,244 112,244 132,177" fill="url(#photo-keys)" role="img" aria-label="Foto: Tastatur mit grüner Login-Taste"/>
        <polygon points="356,110 493,110 493,244 356,244 376,177" fill="url(#photo-woman)" role="img" aria-label="Foto: Frau hält Geldscheine und Gutscheinkarte"/>
      </g>
      <g fill="var(--brand-green)" stroke="var(--white)" stroke-width="2">
        <circle cx="71" cy="96" r="30"/>
        <circle cx="175" cy="260" r="30"/>
        <circle cx="405" cy="90" r="30"/>
      </g>
      <text class="step-number" x="71" y="108" text-anchor="middle">1</text>
      <text class="step-number" x="175" y="272" text-anchor="middle">2</text>
      <text class="step-number" x="405" y="102" text-anchor="middle">3</text>
    </svg>
    <div class="inside-brand">Bonkarten-Profi</div>
    <p class="step-text one">Wählen Sie auf Unserer Website <strong>www.bonkarten-profi.de</strong> Ihren Geschenkanbieter aus.</p>
    <p class="step-text two">Melden Sie sich <strong>kostenlos</strong> an und geben Sie Ihre Gutschein-Informationen ein</p>
    <p class="step-text three">Ausdrucken und den Gutschein an uns senden. Das Geld erhalten Sie <strong>direkt auf Ihr Konto.</strong></p>
  </section>
  <div class="fold-line" style="left:797px"></div>
  <div class="fold-line" style="left:1044px"></div>
</body>
</html>
```